New web design for tech company

We need a photoshop design for a new home page for our website. We develop software for day traders and offer financal services. We would like to see a design that includes the colors of our logo as well as some darker gray. We'll be doing parallex scrollling, so please keep that in mind.
Reason: Have not come to a final decision yet.
Industry/Entity Type
It Company
Font styles to use
Sans Serif
Colors
0255a3
fbee3f
919191
5c5c5c

```html
<!DOCTYPE html>
<html lang="en">
<head>
<meta charset="utf-8">
<title>Brightline Trading – Home</title>
<link href="https://fonts.googleapis.com/css2?family=Arimo:wght@400;700&family=Roboto+Condensed:wght@400;700&display=swap" rel="stylesheet">
<style>
:root{
  --brand-blue:#0255a3;
  --brand-yellow:#fbee3f;
  --gold:#f5c400;
  --gray:#919191;
  --gray-dark:#5c5c5c;
  --text:#4a4a4a;
  --panel:#f2f2f2;
  --navy:#0a1a3f;
  --date-navy:#0d2a5c;
  --footer:#1c1c1c;
  --white:#fff;
}
*{box-sizing:border-box;margin:0;padding:0}
html,body{width:890px;height:1200px;overflow:hidden;background:#fff}
body{font-family:"Arimo",Arial,sans-serif;color:var(--text)}
.canvas{position:relative;width:890px;height:1200px;overflow:hidden}
.abs{position:absolute}
ul{list-style:none}

/* services band */
.services{position:absolute;left:0;top:34px;width:890px;height:292px;background:var(--panel)}
.col-title{position:absolute;font-family:"Roboto Condensed",sans-serif;font-weight:700;font-size:17px;color:var(--brand-blue)}
.swoosh{position:absolute;width:142px;height:13px}
.check-list li{position:absolute;font-size:10.5px;color:var(--gray-dark);text-transform:uppercase;white-space:nowrap;padding-left:13px}
.check-list li svg{position:absolute;left:0;top:1px;width:10px;height:10px}
.avatar{position:absolute;width:68px;height:68px;border-radius:50%;border:3px solid #fff;box-shadow:0 0 0 1px #ccc;background:radial-gradient(circle at 50% 40%,#e8c2a0,#b98a66 60%,#7d8896)}
.quote-mark{position:absolute;font-family:"Roboto Condensed",sans-serif;font-weight:700;font-size:30px;color:var(--brand-blue);line-height:1}
.quote-text{position:absolute;font-size:10px;line-height:13px;color:var(--gray-dark);width:195px}
.quote-author{position:absolute;font-size:10px;color:var(--brand-blue)}
.read-more{position:absolute;font-size:9.5px;color:#333;text-decoration:underline}
.dots span{position:absolute;width:10px;height:10px;border-radius:50%;background:#3b5cc0}
.dots span.active{background:var(--gold)}

/* platform band */
.platform{position:absolute;left:0;top:326px;width:890px;height:313px;background:linear-gradient(100deg,#0e2450 0%,#0a1733 45%,#050a18 70%,#0d1c44 100%)}
.band-title{position:absolute;font-family:"Roboto Condensed",sans-serif;font-weight:700;font-size:17px;color:var(--white)}
.rule{position:absolute;height:2px;background:var(--white)}
.rule i{position:absolute;left:0;top:0;height:2px;background:var(--brand-yellow)}
.feature{position:absolute;width:139px;height:29px;background:var(--white);border-radius:3px;font-size:10px;color:#333;padding:4px 6px 0 20px;line-height:12px;display:flex;align-items:center}
.feature svg{position:absolute;left:6px;top:9px;width:10px;height:10px}
.field{position:absolute;left:551px;width:251px;background:var(--white);border-radius:3px;font-size:10px;color:var(--gray);padding-left:26px;display:flex;align-items:center}
.field svg{position:absolute;left:9px;width:11px;height:11px}
.btn{position:absolute;background:linear-gradient(#ffe14a,#f2b800);border:1px solid #d9a400;border-radius:3px;font-size:10px;color:#111;display:flex;align-items:center;justify-content:center}

/* news */
.section-title{position:absolute;font-family:"Roboto Condensed",sans-serif;font-weight:700;font-size:26px;color:var(--brand-blue)}
.rule.gray{background:var(--gray)}
.date{position:absolute;left:58px;width:42px;height:51px}
.date .day{height:30px;background:#ececec;font-family:"Roboto Condensed",sans-serif;font-weight:700;font-size:16px;color:#333;display:flex;align-items:center;justify-content:center}
.date .month{height:21px;background:var(--date-navy);font-family:"Roboto Condensed",sans-serif;font-weight:700;font-size:11px;color:var(--white);display:flex;align-items:center;justify-content:center}
.post-text{position:absolute;left:112px;width:310px;font-size:9.5px;line-height:13.5px;color:var(--gray)}
.signup-text{position:absolute;left:492px;top:716px;width:330px;font-size:9.5px;line-height:12.5px;color:var(--gray)}
.email-field{position:absolute;left:492px;top:764px;width:298px;height:34px;border:1px solid #cfcfcf;border-radius:3px;font-size:10px;color:var(--gray);padding-left:11px;display:flex;align-items:center}

/* footer */
.footer{position:absolute;left:0;top:941px;width:890px;height:259px;background:var(--footer)}
.footer-col{position:absolute;top:20px;height:170px;background:#222}
.footer-title{position:absolute;font-size:12px;color:var(--white)}
.link-list li{position:absolute;font-size:10px;color:var(--white);padding-left:11px;white-space:nowrap}
.link-list li::before{content:"";position:absolute;left:0;top:3px;width:4px;height:4px;border-right:1.5px solid #fff;border-top:1.5px solid #fff;transform:rotate(45deg)}
.contact-line{position:absolute;font-size:10px;line-height:12px;color:var(--white)}
.contact-line svg{position:absolute;left:-13px;top:1px;width:10px;height:10px}
.badge{position:absolute;top:1019px;width:64px;height:66px;background:#d9d9d9;padding:4px}
.badge div{width:100%;height:100%}
.copyright{position:absolute;left:55px;top:1169px;font-size:9px;color:var(--white)}
.social{position:absolute;top:1157px;width:32px;height:32px;border-radius:50%;background:#1f56a8;border:2px solid #3c3c3c}
</style>
</head>
<body>
<div class="canvas">

  <!-- services / education / testimonials -->
  <section class="services" aria-label="Services overview"></section>

  <h2 class="col-title" style="left:51px;top:76px">Brokerage Services</h2>
  <svg class="swoosh" style="left:52px;top:102px" viewBox="0 0 142 13"><polygon points="0,0 142,3 10,13" fill="var(--gold)"/></svg>
  <h2 class="col-title" style="left:310px;top:76px">Education</h2>
  <svg class="swoosh" style="left:311px;top:102px" viewBox="0 0 142 13"><polygon points="0,0 142,3 10,13" fill="var(--gold)"/></svg>
  <h2 class="col-title" style="left:526px;top:76px">Testimonials</h2>
  <svg class="swoosh" style="left:527px;top:102px" viewBox="0 0 142 13"><polygon points="0,0 142,3 10,13" fill="var(--gold)"/></svg>

  <svg width="0" height="0" style="position:absolute"><defs><symbol id="tick" viewBox="0 0 10 10"><path d="M1 5.5 L4 8.5 L9 1.5" fill="none" stroke="#444" stroke-width="2"/></symbol></defs></svg>

  <ul class="check-list">
    <li style="left:65px;top:141px"><svg><use href="#tick"/></svg>Risk Management Tools</li>
    <li style="left:65px;top:165px"><svg><use href="#tick"/></svg>Trading Groups &amp; Instititions</li>
    <li style="left:65px;top:190px"><svg><use href="#tick"/></svg>Accounts</li>
    <li style="left:65px;top:214px"><svg><use href="#tick"/></svg>Cleint Center Tour</li>
    <li style="left:65px;top:239px"><svg><use href="#tick"/></svg>Funding Instructions</li>
  </ul>
  <ul class="check-list">
    <li style="left:324px;top:141px"><svg><use href="#tick"/></svg>Trading Eductaion</li>
    <li style="left:324px;top:165px"><svg><use href="#tick"/></svg>Trade Ideas</li>
    <li style="left:324px;top:190px"><svg><use href="#tick"/></svg>Video Library</li>
    <li style="left:324px;top:214px"><svg><use href="#tick"/></svg>Live Webinars</li>
    <li style="left:324px;top:239px"><svg><use href="#tick"/></svg>Recorded Webinars</li>
    <li style="left:324px;top:263px"><svg><use href="#tick"/></svg>Online Trading Partners</li>
  </ul>

  <div class="avatar" style="left:527px;top:128px" role="img" aria-label="Portrait of client"></div>
  <span class="quote-mark" style="left:605px;top:133px">&ldquo;</span>
  <p class="quote-text" style="left:627px;top:142px">Lorem ipsum dolor sit amet, consectetur adip isicing elit. Nulla blandit, massa vitae</p>
  <p class="quote-author" style="left:627px;top:172px">Daniel Reyes, CEO Northwave Labs</p>

  <div class="avatar" style="left:527px;top:207px" role="img" aria-label="Portrait of client"></div>
  <span class="quote-mark" style="left:605px;top:212px">&ldquo;</span>
  <p class="quote-text" style="left:627px;top:222px">Lorem ipsum dolor sit amet, consectetur adip isicing elit. Nulla blandit, massa vitae</p>
  <p class="quote-author" style="left:627px;top:251px">Daniel Reyes, CEO Northwave Labs</p>

  <a class="read-more" style="left:728px;top:279px">Read More Testimonial</a>
  <div class="dots">
    <span style="left:751px;top:299px"></span>
    <span class="active" style="left:765px;top:299px"></span>
    <span style="left:779px;top:299px"></span>
    <span style="left:793px;top:299px"></span>
    <span style="left:807px;top:299px"></span>
  </div>

  <!-- platform features & demo form -->
  <section class="platform" role="img" aria-label="Dark blue background with trading data screens"></section>

  <h2 class="band-title" style="left:54px;top:344px">Brightline Trader Platform Features</h2>
  <div class="rule" style="left:54px;top:374px;width:330px"><i style="width:188px"></i></div>
  <h2 class="band-title" style="left:548px;top:344px">Try A Demo Trading Account</h2>
  <div class="rule" style="left:548px;top:374px;width:274px"><i style="width:187px"></i></div>

  <div class="feature" style="left:59px;top:481px"><svg><use href="#tick"/></svg>Advanced Charting</div>
  <div class="feature" style="left:206px;top:481px"><svg><use href="#tick"/></svg>Complex options Trading</div>
  <div class="feature" style="left:353px;top:481px"><svg><use href="#tick"/></svg>Front end API</div>
  <div class="feature" style="left:59px;top:520px"><svg><use href="#tick"/></svg>Hot Key Shortcuts for all order functions</div>
  <div class="feature" style="left:206px;top:520px"><svg><use href="#tick"/></svg>Customizable Layouts</div>
  <div class="feature" style="left:353px;top:520px"><svg><use href="#tick"/></svg>Complete Stability in even the most</div>

  <div class="field" style="top:394px;height:29px"><svg viewBox="0 0 11 11"><circle cx="5.5" cy="3" r="2.5" fill="#999"/><path d="M1 11 C1 6 10 6 10 11Z" fill="#999"/></svg>Name</div>
  <div class="field" style="top:433px;height:29px"><svg viewBox="0 0 11 11"><rect x="0.5" y="2" width="10" height="7" fill="#999"/><path d="M0.5 2 L5.5 6 L10.5 2" fill="none" stroke="#fff"/></svg>Email</div>
  <div class="field" style="top:471px;height:29px"><svg viewBox="0 0 11 11"><path d="M1 4 C1 1 10 1 10 4 L8 4 L8 3 L3 3 L3 4Z" fill="#999"/><rect x="2" y="5" width="7" height="5" fill="#999"/></svg>Phone</div>
  <div class="field" style="top:510px;height:70px;align-items:flex-start;padding-top:10px"><svg viewBox="0 0 11 11" style="top:10px"><rect x="0.5" y="1.5" width="8" height="9" fill="none" stroke="#999"/><path d="M4 7 L10 1" stroke="#999" stroke-width="1.8"/></svg>Address</div>
  <div class="btn" style="left:551px;top:591px;width:87px;height:26px">Submit</div>

  <!-- latest post / newsletter -->
  <h2 class="section-title" style="left:54px;top:657px">LATEST POST</h2>
  <div class="rule gray" style="left:54px;top:696px;width:398px"><i style="width:188px"></i></div>
  <h2 class="section-title" style="left:486px;top:657px">STAY UP TO DATE</h2>
  <div class="rule gray" style="left:486px;top:696px;width:336px"><i style="width:188px"></i></div>

  <div class="date" style="top:717px"><div class="day">10</div><div class="month">APRIL</div></div>
  <p class="post-text" style="top:725px">Nulla et ligula eu leo hendrerit tincidunt. Proin et arcu nec tellus dignissim vehicula. Sed ac libero sit amet turpis dapibus volutpat et in turpis. Morbi dictum, enim interdum venenatis facilisis, mi odio sollicitudin sapien</p>
  <div class="date" style="top:786px"><div class="day">10</div><div class="month">APRIL</div></div>
  <p class="post-text" style="top:792px">Nulla et ligula eu leo hendrerit tincidunt. Proin et arcu nec tellus dignissim vehicula. Sed ac libero sit amet turpis dapibus volutpat et in turpis. Morbi dictum, enim interdum venenatis facilisis, mi odio sollicitudin sapien</p>
  <div class="date" style="top:856px"><div class="day">10</div><div class="month">APRIL</div></div>
  <p class="post-text" style="top:863px">Nulla et ligula eu leo hendrerit tincidunt. Proin et arcu nec tellus dignissim vehicula. Sed ac libero sit amet turpis dapibus volutpat et in turpis. Morbi dictum, enim interdum venenatis facilisis, mi odio sollicitudin sapien</p>

  <p class="signup-text">Find out new features and get releases as they happen. Your email will only ewver be used for first party news relating jobs, nothing else.</p>
  <div class="email-field">Type your email id here</div>
  <div class="btn" style="left:492px;top:812px;width:87px;height:27px">Submit</div>

  <!-- footer -->
  <footer class="footer"></footer>
  <div class="footer-col" style="left:58px;top:961px;width:160px"></div>
  <div class="footer-col" style="left:249px;top:961px;width:170px"></div>
  <div class="footer-col" style="left:432px;top:961px;width:200px"></div>
  <div class="footer-col" style="left:660px;top:961px;width:160px"></div>

  <h3 class="footer-title" style="left:58px;top:959px">Quick Links</h3>
  <h3 class="footer-title" style="left:249px;top:959px">Legal</h3>
  <h3 class="footer-title" style="left:442px;top:959px">Contact Information</h3>
  <h3 class="footer-title" style="left:666px;top:959px">Blogs</h3>

  <ul class="link-list">
    <li style="left:68px;top:994px">Home</li>
    <li style="left:68px;top:1014px">Trading Platform</li>
    <li style="left:68px;top:1035px">Pricing</li>
    <li style="left:68px;top:1055px">Brokerage Service</li>
    <li style="left:68px;top:1075px">Education</li>
    <li style="left:68px;top:1095px">About</li>
  </ul>
  <ul class="link-list">
    <li style="left:260px;top:994px">Disclosure</li>
    <li style="left:260px;top:1014px">Fix RA</li>
    <li style="left:260px;top:1035px">SRC</li>
    <li style="left:260px;top:1055px">SRC Order Routing</li>
    <li style="left:260px;top:1075px">procedure</li>
    <li style="left:260px;top:1095px">Forex Risk Disclosure</li>
  </ul>

  <p class="contact-line" style="left:464px;top:994px"><svg viewBox="0 0 10 10"><path d="M5 10 L1.5 5 A4 4 0 1 1 8.5 5Z" fill="#fff"/><circle cx="5" cy="3.6" r="1.4" fill="#1c1c1c"/></svg>42 Harbor View Lane,<br>Eastgate Park 40512 , Avalon</p>
  <p class="contact-line" style="left:464px;top:1027px"><svg viewBox="0 0 10 10"><rect x="3" y="0.5" width="4" height="9" rx="0.8" fill="none" stroke="#fff"/></svg>555 018 2046</p>
  <p class="contact-line" style="left:464px;top:1054px"><svg viewBox="0 0 10 10"><rect x="0.5" y="2" width="9" height="6.5" fill="none" stroke="#fff"/><path d="M0.5 2 L5 6 L9.5 2" fill="none" stroke="#fff"/></svg>info@brightlinetrading.example</p>

  <p class="contact-line" style="left:669px;top:994px">Active Trading Blog</p>
  <div class="badge" style="left:672px"><div style="background:#20365e" role="img" aria-label="Broker award badge"></div></div>
  <div class="badge" style="left:739px"><div style="background:#f4f4f4" role="img" aria-label="Broker review badge"></div></div>

  <p class="copyright">Copyright © 2011-2014, Meridian Market Systems Inc. All Rights Reserved</p>
  <span class="social" style="left:634px" aria-label="Social profile"></span>
  <span class="social" style="left:676px;background:#1c8fd6" aria-label="Social profile"></span>
  <span class="social" style="left:717px;background:#1470a8" aria-label="Social profile"></span>

</div>
</body>
</html>
```